Linden Medical - Flyer

We are a full service pharmacy that specializes in diabetic testing and medications. We research the patient's insurance to maximize their insurance benefit and then deliver the medications monthly directly to the patient's doorstep, for free! We save the patient, time and money every month.
We would love a flyer that we can distribute to Doctor's offices and patients that sum up our pharmacy. Emphasis on saving money, time, and getting the best quality supplies by maximizing their insurance. We want it to be eye catching, clean, and professional.
You can use our logo or feel free to make your own design.
Updates
Target Market(s)
diabetic patients wanting to save money
Industry/Entity Type
Insurance
Look and feel
Each slider illustrates characteristics of the customer's brand and the style your logo design should communicate.

```html
<!DOCTYPE html>
<html lang="en">
<head>
<meta charset="utf-8">
<title>Linden Medical – Flyer</title>
<link href="https://fonts.googleapis.com/css2?family=Arimo:wght@400;700&display=swap" rel="stylesheet">
<style>
  :root {
    --stage: #1b1f1e;
    --sky-top: #cfe9ee;
    --sky-mid: #eef8fa;
    --sky-low: #ffffff;
    --leaf: #7cb82f;
    --leaf-dark: #5f9a1e;
    --leaf-text: #5a9a1a;
    --alert: #c4161c;
    --teal: #2a9bb5;
    --ink: #1d1d1d;
    --orange: #ea7a12;
    --orange-light: #f6a23a;
    --white: #ffffff;
    --brand: #3a4a4f;
  }
  * { box-sizing: border-box; margin: 0; padding: 0; }
  html, body { width: 1200px; height: 1019px; overflow: hidden; }
  body {
    background: var(--stage);
    font-family: "Arimo", Arial, sans-serif;
    color: var(--ink);
    position: relative;
  }
  .flyer {
    position: absolute;
    width: 541px;
    height: 701px;
    overflow: hidden;
    background: radial-gradient(ellipse at 60% 35%, var(--sky-mid) 0%, var(--sky-top) 55%, #bfe0e7 100%);
  }
  .flyer--front { left: 57px; top: 167px; }
  .flyer--back { left: 612px; top: 165px; }
  .flyer > * { position: absolute; }

  .band { left: 0; top: 0; width: 541px; height: 701px; }

  .brand {
    display: flex; align-items: center; gap: 10px;
    color: var(--brand); font-weight: 400; letter-spacing: 2px;
    text-transform: uppercase; white-space: nowrap;
  }
  .brand__dot { width: 26px; height: 26px; border-radius: 50%; background: var(--leaf); }
  .flyer--front .brand { left: 0; width: 541px; top: 44px; justify-content: center; font-size: 34px; }
  .flyer--back .brand { left: 300px; top: 540px; font-size: 21px; gap: 8px; }
  .flyer--back .brand__dot { width: 20px; height: 20px; }

  .headline {
    left: 0; width: 541px; top: 143px;
    text-align: center; font-size: 22px; line-height: 32px;
  }
  .headline .hl-green { color: var(--leaf-text); font-weight: 700; }
  .headline .hl-red { color: var(--alert); font-weight: 700; }

  .benefit { display: flex; align-items: center; gap: 15px; font-size: 20px; line-height: 24px; text-transform: uppercase; }
  .benefit__icon {
    width: 68px; height: 68px; border-radius: 50%;
    background: radial-gradient(circle at 40% 35%, var(--orange-light), var(--orange));
    flex: none;
  }
  .benefit--meter { left: 75px; top: 243px; }
  .benefit--money { left: 288px; top: 243px; }
  .benefit--time { left: 75px; top: 344px; }
  .benefit--delivery { left: 288px; top: 344px; }

  .photo-fingers {
    left: 86px; top: 479px; width: 237px; height: 150px;
    border-radius: 40px 40px 0 0;
    background: linear-gradient(180deg, #f1c8ad 0%, #e2a888 100%);
  }

  .giftcard {
    width: 165px; height: 105px; border-radius: 8px;
    padding: 12px 14px; text-align: right;
  }
  .giftcard__label { font-size: 12px; font-weight: 700; }
  .giftcard__amount { font-size: 38px; font-weight: 700; line-height: 44px; text-align: center; }
  .giftcard__note { font-size: 11px; text-align: center; }
  .giftcard--orange {
    left: 336px; top: 497px; transform: rotate(-20deg);
    background: linear-gradient(160deg, var(--orange-light), var(--orange));
    color: var(--white); box-shadow: 0 6px 10px rgba(0,0,0,.2);
  }
  .giftcard--white {
    left: 326px; top: 378px; transform: rotate(-18deg);
    background: linear-gradient(160deg, #ffffff, #dcdcdc);
    color: var(--alert); box-shadow: 0 6px 10px rgba(0,0,0,.25);
  }
  .giftcard--white .giftcard__note { color: #555; }

  .contact { left: 0; width: 541px; text-align: center; color: var(--white); }
  .contact--phone { top: 636px; font-size: 17px; font-weight: 700; }
  .contact--phone b { font-size: 27px; }
  .contact--web { top: 672px; font-size: 19px; }

  .intro { left: 42px; width: 470px; font-size: 16px; line-height: 23px; color: var(--ink); }
  .intro strong { color: var(--teal); font-size: 19px; }
  .intro--1 { top: 24px; }
  .intro--2 { top: 90px; }
  .intro--3 { top: 156px; }
  .intro--4 { top: 221px; }

  .cta-title { left: 42px; top: 286px; font-size: 27px; font-weight: 700; color: var(--alert); }
  .cta-text { left: 42px; top: 320px; font-size: 18px; line-height: 23px; width: 420px; }

  .figure-celebrate {
    left: 83px; top: 414px; width: 187px; height: 209px;
    background: linear-gradient(180deg, #3a3a3a, #151515);
    border-radius: 50% 50% 10px 10px / 30% 30% 10px 10px;
  }
  .heart-mark {
    left: 6px; top: 596px; width: 77px; height: 82px; border-radius: 40%;
    background: linear-gradient(160deg, #e8262a, #8cc63f);
  }
  .brand-web { left: 292px; top: 596px; width: 200px; text-align: center; font-size: 16px; color: var(--brand); }
  .flyer--back .contact--phone { top: 657px; font-size: 27px; }
</style>
</head>
<body>

<section class="flyer flyer--front">
  <svg class="band" viewBox="0 0 541 701" aria-hidden="true">
    <path d="M0 628 Q300 610 541 506 L541 701 L0 701 Z" fill="var(--leaf)"/>
    <path d="M0 628 Q300 610 541 506 L541 520 Q300 625 0 640 Z" fill="var(--leaf-dark)" opacity=".35"/>
  </svg>

  <div class="brand"><span class="brand__dot"></span>Linden Medical</div>

  <h1 class="headline">Are the costs of your <span class="hl-green">Diabetic Testing</span><br>supplies as high as your <span class="hl-red">Blood Sugar?</span></h1>

  <div class="benefit benefit--meter"><span class="benefit__icon" role="img" aria-label="Compass icon"></span><span>Free<br>Meter</span></div>
  <div class="benefit benefit--money"><span class="benefit__icon" role="img" aria-label="Wallet with cash icon"></span><span>Save<br>Money</span></div>
  <div class="benefit benefit--time"><span class="benefit__icon" role="img" aria-label="Alarm clock icon"></span><span>Save<br>Time</span></div>
  <div class="benefit benefit--delivery"><span class="benefit__icon" role="img" aria-label="Briefcase with arrow icon"></span><span>Free<br>Delivery</span></div>

  <div class="photo-fingers" role="img" aria-label="Photo of four fingertips drawn as a smiling family"></div>

  <div class="giftcard giftcard--orange">
    <div class="giftcard__label">Gift Card</div>
    <div class="giftcard__amount">$20</div>
    <div class="giftcard__note">given your first order</div>
  </div>

  <p class="contact contact--phone">Toll Free Number <b>13579246</b></p>
  <p class="contact contact--web">www.lindenmedical.com</p>
</section>

<section class="flyer flyer--back">
  <svg class="band" viewBox="0 0 541 701" aria-hidden="true">
    <path d="M0 530 Q160 640 541 605 L541 701 L0 701 Z" fill="var(--leaf)"/>
    <path d="M0 530 Q160 640 541 605 L541 618 Q160 655 0 545 Z" fill="var(--leaf-dark)" opacity=".35"/>
  </svg>

  <p class="intro intro--1">We are a full service pharmacy that specializes in <strong>diabetic testing</strong> supplies and oral medications.</p>
  <p class="intro intro--2">We research <strong>your insurance</strong> to determine how to save you the most money</p>
  <p class="intro intro--3">We then contact your physician to get the <strong>appropriate authorization</strong></p>
  <p class="intro intro--4">We ship your testing supplies and oral medications directly to your home for <strong>free!</strong></p>

  <h2 class="cta-title">Get started Today!</h2>
  <p class="cta-text">Call our toll free number OR go to our website and fill our form.</p>

  <div class="figure-celebrate" role="img" aria-label="Illustration of a businessman in a suit raising both arms in celebration"></div>

  <div class="giftcard giftcard--white">
    <div class="giftcard__label">Gift Card</div>
    <div class="giftcard__amount">$20</div>
    <div class="giftcard__note">given your first order</div>
  </div>

  <div class="brand"><span class="brand__dot"></span>Linden Medical</div>
  <p class="brand-web">www.lindenmedical.com</p>

  <div class="heart-mark" role="img" aria-label="Red heart resting in a green hand"></div>

  <p class="contact contact--phone">Toll Free Number 13579246</p>
</section>

</body>
</html>
```